Baby Boutique Needs a Business Card Design

We need a modern double sided business card design using the attached logo for Lil' Tot Nook.

Lil' Tot Nook is a baby boutique which sells only handmade clothing and accessories for both boys and girls. Our store will live exclusively online.

We would like to only use the colors that have been used in the logo.

Target Market(s)

Potential wholesale clients, Small business owners

Industry/Entity Type

Retail

Contact Information for Business Card

Name Wendell J. Ferris (Owner)
Email sales@ltotnook.com
Main Phone 787-203-6159
Cell phone 787-203-6742
Website www.LTotNook.com

Font styles to use
Sans Serif

Colors

Designer to choose colors to be used in the design.

Requirements
Must have
• -Would like to have icons that indentify the contact information.
• -Include our website
• -Include our tagline in a small area near the bottom. "Handmade Baby Creations"
• -Would like to include Facebook and Instagram Icons
• -
Nice to have
• Would like to have a simple back side with the logo.
• Something along the lines of the harbor ledger card attached.

```html
<!DOCTYPE html>
<html lang="en">
<head>
<meta charset="utf-8">
<title>Lil' Tot Nook — Business Card</title>
<link href="https://fonts.googleapis.com/css2?family=Rubik:wght@400;500;700&display=swap" rel="stylesheet">
<style>
  :root {
    --stage: #1a1b1b;
    --teal: #7acabe;
    --coral: #dd5c5c;
    --paper: #ffffff;
    --ink: #3a3a3a;
    --muted: #555555;
  }
  * { box-sizing: border-box; margin: 0; padding: 0; }
  html, body { width: 1200px; height: 1000px; overflow: hidden; background: var(--stage); }
  body { font-family: "Rubik", Arial, sans-serif; position: relative; }

  .card {
    position: absolute;
    left: 285px;
    width: 630px;
    height: 360px;
    border-radius: 22px;
    overflow: hidden;
  }

  /* Logo side */
  .card-front { top: 110px; background: var(--teal); }
  .card-front .brand {
    position: absolute; left: 0; right: 0; top: 105px;
    text-align: center;
    font-weight: 700; font-size: 64px; line-height: 1;
    color: var(--paper);
  }
  .card-front .brand-art {
    position: absolute; left: 230px; top: 200px; width: 170px; height: 52px;
    border-radius: 26px;
    background: linear-gradient(90deg, rgba(255,255,255,0.35), rgba(255,255,255,0.6));
  }

  /* Contact side */
  .card-back { top: 530px; background: var(--paper); }
  .holder { position: absolute; left: 44px; top: 38px; }
  .holder-name { font-weight: 700; font-size: 25px; color: var(--coral); letter-spacing: 0.5px; }
  .holder-role { font-size: 16px; color: var(--muted); margin-top: 2px; }

  .contacts { position: absolute; left: 44px; top: 160px; list-style: none; }
  .contacts li {
    display: flex; align-items: center; gap: 12px;
    font-size: 20px; color: var(--ink); height: 30px; letter-spacing: 0.5px;
  }
  .contacts svg { width: 18px; height: 18px; flex: none; }

  .brand-mark { position: absolute; right: 40px; top: 58px; width: 220px; text-align: center; }
  .brand-mark .brand { font-weight: 700; font-size: 38px; line-height: 1.05; color: var(--teal); }
  .brand-mark .brand-art {
    margin: 12px auto 0; width: 170px; height: 44px; border-radius: 22px;
    background: linear-gradient(90deg, #f0b3b3, var(--coral));
  }

  .social { position: absolute; right: 24px; top: 250px; display: flex; gap: 10px; }
  .social span { width: 30px; height: 30px; border-radius: 50%; background: var(--coral); }

  .rule { position: absolute; left: 0; right: 0; top: 292px; height: 5px; background: var(--teal); }
  .footer-band {
    position: absolute; left: 0; right: 0; bottom: 0; height: 58px;
    background: var(--coral); color: var(--paper);
    display: flex; align-items: center; justify-content: center;
    font-size: 20px; letter-spacing: 0.5px;
  }
</style>
</head>
<body>

  <section class="card card-front" aria-label="Card front">
    <div class="brand">Lil' Tot Nook</div>
    <div class="brand-art" role="img" aria-label="Line drawing of a stork carrying a bundle"></div>
  </section>

  <section class="card card-back" aria-label="Card back">
    <div class="holder">
      <div class="holder-name">Wendell J. Ferris</div>
      <div class="holder-role">Owner</div>
    </div>

    <ul class="contacts">
      <li>
        <svg viewBox="0 0 24 24" aria-hidden="true"><path d="M6.6 10.8a15 15 0 0 0 6.6 6.6l2.2-2.2a1 1 0 0 1 1-.25 11 11 0 0 0 3.6.6 1 1 0 0 1 1 1V20a1 1 0 0 1-1 1A17 17 0 0 1 3 4a1 1 0 0 1 1-1h3.5a1 1 0 0 1 1 1 11 11 0 0 0 .6 3.6 1 1 0 0 1-.25 1z" fill="#dd5c5c"/></svg>
        787-203-6159
      </li>
      <li>
        <svg viewBox="0 0 24 24" aria-hidden="true"><rect x="6" y="2" width="12" height="20" rx="2" fill="none" stroke="#dd5c5c" stroke-width="2"/><circle cx="12" cy="18" r="1.2" fill="#dd5c5c"/></svg>
        787-203-6742
      </li>
      <li>
        <svg viewBox="0 0 24 24" aria-hidden="true"><g fill="none" stroke="#dd5c5c" stroke-width="1.8"><circle cx="12" cy="12" r="9"/><ellipse cx="12" cy="12" rx="4" ry="9"/><path d="M3 12h18M5 7h14M5 17h14"/></g></svg>
        www.LTotNook.com
      </li>
    </ul>

    <div class="brand-mark">
      <div class="brand">Lil' Tot Nook</div>
      <div class="brand-art" role="img" aria-label="Line drawing of a stork carrying a bundle"></div>
    </div>

    <div class="social" aria-label="Social profiles">
      <span></span><span></span>
    </div>

    <div class="rule"></div>
    <div class="footer-band">Handmade Baby Creations</div>
  </section>

</body>
</html>
```